Energieausweis
Zielgruppe
Zielgruppe sind Immobilieninteressenten - Verwendung in einem Immobilienmagazin und im Internet.
Aufgabenstellung
Ab dem 1. Mai muss in Deutschland die Energie-Effizienzklasse bei Immobilienangeboten mit veröffentlicht werden. Das kann man nüchtern in Zahlen darstellen, aber auch in einer netten Grafik. In der Anlage finden 2 von uns gekaufte Pixbarun-Bilder. Das Bild mit dem Männchen ist eine sehr nette Idee. Da wir in unserem Logo auch ein Männchen haben, bietet es sich an, ein LindenHaus-Männchen zusammen mit der bunten Grafik zu gestalten. (Das Pixbarun-Bild soll nur die Idee erklären - bitte nicht verwenden). Wenn die Grafik fertig ist, legen wir einen Pfeil zur Kennzeichnung der jeweiligen Energieklasse hinzu. Das heisst, wir haben dann für jede Energieklasse eine entsprechende Vorlage und dem richtig platzierten Pfeil. Weiter finden sie in der Anlage unser Firmenlogo zur freuen Verwendung.

```html
<!DOCTYPE html>
<html lang="de">
<head>
<meta charset="utf-8">
<title>Energieausweis – Vorlagen A bis G</title>
<link rel="stylesheet" href="https://fonts.googleapis.com/css2?family=Signika:wght@400;600&display=swap">
<style>
  :root {
    --ink-blue: #0b4d80;
    --figure-blue: #0d4a7a;
    --card-border: #d2d2d2;
    --card-edge: #e8e8e8;
    --class-a: #0a6b35;
    --class-b: #27a038;
    --class-c: #9dbe10;
    --class-d: #e2d812;
    --class-e: #edb906;
    --class-f: #ec7407;
    --class-g: #e2231f;
    --tag: #000;
    --caption: #1a1a1a;
  }
  html, body {
    margin: 0;
    padding: 0;
    width: 777px;
    height: 1200px;
    overflow: hidden;
    background: #fff;
    font-family: "Signika", sans-serif;
  }
  .sheet { position: relative; width: 777px; height: 1200px; }
  .certificate {
    position: absolute;
    width: 360px;
    height: 277px;
    box-sizing: border-box;
    border: 1.5px solid var(--card-border);
    border-radius: 6px;
    box-shadow: -2px -2px 0 var(--card-edge);
    background: #fff;
  }
  .certificate__title {
    position: absolute;
    left: 12px;
    top: 8px;
    margin: 0;
    font-weight: 400;
    font-size: 25px;
    letter-spacing: 1.2px;
    color: var(--ink-blue);
    line-height: 1;
  }
  .certificate__caption {
    position: absolute;
    left: 12px;
    top: 247px;
    margin: 0;
    font-weight: 600;
    font-size: 13px;
    color: var(--caption);
  }
  .certificate__graphic { position: absolute; left: 0; top: 0; }
  .scale-letter { font-family: "Signika", sans-serif; font-weight: 600; font-size: 20px; fill: #fff; }
  .tag-letter { font-family: "Signika", sans-serif; font-weight: 600; font-size: 18px; fill: #fff; }
  .col-1 { left: 15px; }
  .col-2 { left: 401px; }
  .row-1 { top: 17px; }
  .row-2 { top: 308px; }
  .row-3 { top: 612px; }
  .row-4 { top: 905px; }
</style>
</head>
<body>
<svg width="0" height="0" style="position:absolute" aria-hidden="true">
  <defs>
    <symbol id="efficiency-scale" viewBox="0 0 426 328">
      <rect x="14" y="60" width="124" height="220" rx="10" fill="var(--figure-blue)" role="img" aria-label="Illustration: Männchen, das die Energieskala trägt"/>
      <polygon points="138,62 238,62 252,76 238,90 138,90" fill="var(--class-a)"/>
      <polygon points="138,93 252,93 266,107 252,121 138,121" fill="var(--class-b)"/>
      <polygon points="138,124 267,124 281,138 267,152 138,152" fill="var(--class-c)"/>
      <polygon points="138,155 281,155 295,169 281,183 138,183" fill="var(--class-d)"/>
      <polygon points="138,186 296,186 310,200 296,214 138,214" fill="var(--class-e)"/>
      <polygon points="138,217 310,217 324,231 310,245 138,245" fill="var(--class-f)"/>
      <polygon points="138,248 325,248 339,262 325,276 138,276" fill="var(--class-g)"/>
      <text class="scale-letter" x="218" y="83" text-anchor="middle">A</text>
      <text class="scale-letter" x="218" y="114" text-anchor="middle">B</text>
      <text class="scale-letter" x="218" y="145" text-anchor="middle">C</text>
      <text class="scale-letter" x="218" y="176" text-anchor="middle">D</text>
      <text class="scale-letter" x="218" y="207" text-anchor="middle">E</text>
      <text class="scale-letter" x="218" y="238" text-anchor="middle">F</text>
      <text class="scale-letter" x="218" y="269" text-anchor="middle">G</text>
    </symbol>
    <symbol id="house" viewBox="-28 -40 56 52" overflow="visible">
      <path d="M0,-38 L12,-27 L12,-36 L18,-36 L18,-21 L26,-14 L19,-14 L19,10 L-19,10 L-19,-14 L-26,-14 Z" fill="currentColor"/>
      <rect x="-11" y="-3" width="8" height="13" fill="#fff"/>
    </symbol>
  </defs>
</svg>

<main class="sheet">
  <!-- Class A -->
  <section class="certificate col-1 row-1">
    <svg class="certificate__graphic" width="360" height="277" viewBox="0 0 426 328">
      <use href="#efficiency-scale" x="0" y="0" width="426" height="328"/>
      <g transform="translate(0,76)">
        <polygon points="288,0 300,-10 352,-10 352,10 300,10" fill="var(--tag)"/>
        <text class="tag-letter" x="340" y="6" text-anchor="middle">A</text>
        <use href="#house" x="346" y="-40" width="56" height="52" style="color:var(--class-a)"/>
      </g>
    </svg>
    <h2 class="certificate__title">ENERGIEAUSWEIS</h2>
    <p class="certificate__caption">Berechneter Energiebedarf</p>
  </section>

  <!-- Class B -->
  <section class="certificate col-2 row-1">
    <svg class="certificate__graphic" width="360" height="277" viewBox="0 0 426 328">
      <use href="#efficiency-scale" x="0" y="0" width="426" height="328"/>
      <g transform="translate(0,107)">
        <polygon points="288,0 300,-10 352,-10 352,10 300,10" fill="var(--tag)"/>
        <text class="tag-letter" x="340" y="6" text-anchor="middle">B</text>
        <use href="#house" x="346" y="-40" width="56" height="52" style="color:var(--class-b)"/>
      </g>
    </svg>
    <h2 class="certificate__title">ENERGIEAUSWEIS</h2>
    <p class="certificate__caption">Berechneter Energiebedarf</p>
  </section>

  <!-- Class C -->
  <section class="certificate col-1 row-2">
    <svg class="certificate__graphic" width="360" height="277" viewBox="0 0 426 328">
      <use href="#efficiency-scale" x="0" y="0" width="426" height="328"/>
      <g transform="translate(0,138)">
        <polygon points="288,0 300,-10 352,-10 352,10 300,10" fill="var(--tag)"/>
        <text class="tag-letter" x="340" y="6" text-anchor="middle">C</text>
        <use href="#house" x="346" y="-40" width="56" height="52" style="color:var(--class-c)"/>
      </g>
    </svg>
    <h2 class="certificate__title">ENERGIEAUSWEIS</h2>
    <p class="certificate__caption">Berechneter Energiebedarf</p>
  </section>

  <!-- Class D -->
  <section class="certificate col-2 row-2">
    <svg class="certificate__graphic" width="360" height="277" viewBox="0 0 426 328">
      <use href="#efficiency-scale" x="0" y="0" width="426" height="328"/>
      <g transform="translate(0,169)">
        <polygon points="288,0 300,-10 352,-10 352,10 300,10" fill="var(--tag)"/>
        <text class="tag-letter" x="340" y="6" text-anchor="middle">D</text>
        <use href="#house" x="346" y="-40" width="56" height="52" style="color:var(--class-d)"/>
      </g>
    </svg>
    <h2 class="certificate__title">ENERGIEAUSWEIS</h2>
    <p class="certificate__caption">Berechneter Energiebedarf</p>
  </section>

  <!-- Class E -->
  <section class="certificate col-1 row-3">
    <svg class="certificate__graphic" width="360" height="277" viewBox="0 0 426 328">
      <use href="#efficiency-scale" x="0" y="0" width="426" height="328"/>
      <g transform="translate(0,200)">
        <polygon points="288,0 300,-10 352,-10 352,10 300,10" fill="var(--tag)"/>
        <text class="tag-letter" x="340" y="6" text-anchor="middle">E</text>
        <use href="#house" x="346" y="-40" width="56" height="52" style="color:var(--class-e)"/>
      </g>
    </svg>
    <h2 class="certificate__title">ENERGIEAUSWEIS</h2>
    <p class="certificate__caption">Berechneter Energiebedarf</p>
  </section>

  <!-- Class F -->
  <section class="certificate col-2 row-3">
    <svg class="certificate__graphic" width="360" height="277" viewBox="0 0 426 328">
      <use href="#efficiency-scale" x="0" y="0" width="426" height="328"/>
      <g transform="translate(0,231)">
        <polygon points="288,0 300,-10 352,-10 352,10 300,10" fill="var(--tag)"/>
        <text class="tag-letter" x="340" y="6" text-anchor="middle">F</text>
        <use href="#house" x="346" y="-40" width="56" height="52" style="color:var(--class-f)"/>
      </g>
    </svg>
    <h2 class="certificate__title">ENERGIEAUSWEIS</h2>
    <p class="certificate__caption">Berechneter Energiebedarf</p>
  </section>

  <!-- Class G -->
  <section class="certificate col-1 row-4">
    <svg class="certificate__graphic" width="360" height="277" viewBox="0 0 426 328">
      <use href="#efficiency-scale" x="0" y="0" width="426" height="328"/>
      <g transform="translate(0,262)">
        <polygon points="288,0 300,-10 352,-10 352,10 300,10" fill="var(--tag)"/>
        <text class="tag-letter" x="340" y="6" text-anchor="middle">G</text>
        <use href="#house" x="346" y="-40" width="56" height="52" style="color:var(--class-g)"/>
      </g>
    </svg>
    <h2 class="certificate__title">ENERGIEAUSWEIS</h2>
    <p class="certificate__caption">Berechneter Energiebedarf</p>
  </section>
</main>
</body>
</html>
```